Letterhead & Business Card Design Project

Use existing logo to create a new letterhead and business card design. Looking for something clean modern using color options of black, white and gray. The green from the logo may be used lightly as an accent color.

Target Market(s)

Professional business people

Industry/Entity Type

Business

Requirements
Must have
• Business card with front and back design using existing logo.
Nice to have
• Professional presentation
Clean look
Should not have
• No oil rigs, pumpjacks or clip art.

```html
<!DOCTYPE html>
<html lang="en">
<head>
<meta charset="utf-8">
<title>Meridian Exploration Stationery</title>
<link href="https://fonts.googleapis.com/css2?family=Cormorant+Garamond:wght@400;500&display=swap" rel="stylesheet">
<style>
:root{
  --stage:#e6e3df;
  --paper:#ffffff;
  --ink:#1a1a1a;
  --gray:#7a7a7a;
  --soft-gray:#8c8c8c;
  --accent:#4cb84a;
}
*{margin:0;padding:0;box-sizing:border-box}
html,body{width:1200px;height:1000px;overflow:hidden}
body{background:var(--stage);font-family:"Cormorant Garamond",Georgia,serif;font-variant-numeric:lining-nums;position:relative;color:var(--ink)}
.sheet{position:absolute;background:var(--paper);box-shadow:0 2px 6px rgba(0,0,0,.18)}
.letterhead{left:56px;top:22px;width:660px;height:943px}
.wordmark{position:absolute;left:0;right:0;text-align:center;color:var(--ink);font-weight:400;line-height:1;white-space:nowrap}
.letterhead .wordmark{top:50px;font-size:38px;letter-spacing:3px}
.letterhead-footer{position:absolute;left:104px;top:862px;width:448px}
.accent-rule{height:2px;background:linear-gradient(90deg,rgba(76,184,74,0),var(--accent) 12%,var(--accent) 88%,rgba(76,184,74,0))}
.footer-cols{display:flex;gap:40px;margin:16px 0 0 59px;font-size:13px;letter-spacing:1px;color:var(--gray);line-height:16.5px}
.footer-address{font-style:normal;width:146px}
.contact-line{display:flex;align-items:center;gap:6px}
.contact-line svg{width:10px;height:10px;fill:#222}
.card-front{left:760px;top:92px;width:354px;height:202px}
.card-back{left:763px;top:312px;width:354px;height:201px}
.holder{position:absolute;left:10px;right:26px;top:58px;text-align:center}
.holder-name{font-size:23px;letter-spacing:1px;line-height:1;padding-bottom:6px}
.holder .accent-rule{margin:0 0 4px}
.holder-title{font-size:16px;letter-spacing:1.5px;color:var(--soft-gray);line-height:18px}
.holder-cell{font-size:23px;letter-spacing:2px;color:var(--gray);line-height:26px}
.card-back .wordmark{top:72px;font-size:30px;letter-spacing:3px}
</style>
</head>
<body>
<section class="sheet letterhead">
  <div class="wordmark">Meridian Exploration</div>
  <footer class="letterhead-footer">
    <div class="accent-rule"></div>
    <div class="footer-cols">
      <address class="footer-address">4210 North Elm Ave,<br>Suite 340,<br>Harlow, Kansas 66012</address>
      <div>
        <div class="contact-line"><svg viewBox="0 0 10 10"><path d="M2 0.5 3.6 2.6 2.6 3.6Q3.6 5.8 6.4 7.4L7.4 6.4 9.5 8 8.4 9.5Q4.5 9 0.5 1.6Z"/></svg>555.302.4418</div>
        <div class="contact-line"><svg viewBox="0 0 10 10"><rect x="2.5" y="0.5" width="5" height="3"/><rect x="0.5" y="3.5" width="9" height="4" rx="1"/><rect x="2.5" y="6.5" width="5" height="3"/></svg>555.302.4419</div>
        <div class="contact-line"><svg viewBox="0 0 10 10"><circle cx="5" cy="5" r="4.5"/><path d="M0.5 5h9M5 0.5v9" stroke="#fff" stroke-width="0.8"/><ellipse cx="5" cy="5" rx="2" ry="4.5" fill="none" stroke="#fff" stroke-width="0.8"/></svg>www.meridianexploration.com</div>
      </div>
    </div>
  </footer>
</section>

<section class="sheet card-front">
  <div class="holder">
    <div class="holder-name">DANIEL R WHITFORD</div>
    <div class="accent-rule"></div>
    <div class="holder-title">Managing Member</div>
    <div class="holder-cell">cell 555.214.7730</div>
  </div>
</section>

<section class="sheet card-back">
  <div class="wordmark">Meridian Exploration</div>
</section>
</body>
</html>
```